Something that stands out and has more of a modern look to it...will be printing on plastic cards so keep in mind and review old business card as reference

Industry/Entity Type

Real Estate Agent

Contact Information for Business Card

Front of business card will have picture and information the back of card can have logo or name in cursive etc

Logo Text

Marcus Belvane

Font styles to use
Decorative
Script

Colors

Designer to choose colors to be used in the design.

Requirements
Must have
• Must have "Harborline 47" logo and state "Quiet Summit Realty Inc Brokerage*" next to it.
• Offices in: Toronto, Markham, Durham
• *Independently Owned and Operated trademarks owned by Harborline 47 Real Estate LLC used under license or authorized sub-license. 2017 Harborline 47 Canada Limited Partnership. (See old business card for reference)
• Email address: marcus@mbelvanehomes.example
• Website: www.MBelvaneHomes.example
• Direct: 647-555-0143
• Name: Marcus Bel Vane
• Office: 905-555-0178
Nice to have
• Maybe a catchy slogan
• One side can have my name designed or the Logo
Should not have
• The Harborline 47 Logo too large or focused on (my business requires me just to have this somewhere on the card).
• Yellow and black theme

```html
<!DOCTYPE html>
<html lang="en">
<head>
<meta charset="utf-8">
<title>Marcus Bel Vane – Business Card</title>
<link rel="stylesheet" href="https://fonts.googleapis.com/css2?family=Lato:wght@400;700;900&display=swap">
<style>
  :root {
    --ink: #14233f;
    --text: #1b1f27;
    --paper: #ffffff;
    --accent: #3f9c9f;
    --bg: #e3e6ea;
    --photo-top: #dfe3e8;
    --photo-mid: #5b6f8f;
    --photo-bottom: #26385f;
  }
  * { box-sizing: border-box; margin: 0; padding: 0; }
  html, body { width: 1200px; height: 680px; overflow: hidden; }
  body {
    background: var(--bg);
    font-family: "Lato", Arial, sans-serif;
    position: relative;
  }
  .card {
    position: absolute;
    top: 185px;
    width: 540px;
    height: 310px;
    overflow: hidden;
    box-shadow: 0 6px 18px rgba(0,0,0,.22);
  }
  .card--front { left: 40px; background: var(--paper); }
  .card--back { left: 620px; background: var(--ink); }

  /* front */
  .portrait {
    position: absolute;
    right: 0; top: 18px;
    width: 210px; height: 250px;
    background: linear-gradient(180deg, var(--photo-top) 0%, var(--photo-mid) 50%, var(--photo-bottom) 100%);
  }
  .swoosh { position: absolute; inset: 0; width: 540px; height: 310px; }
  .swoosh__band { fill: var(--ink); }
  .swoosh__stripe { fill: var(--accent); }

  .agent { position: absolute; left: 26px; top: 30px; width: 290px; color: var(--text); }
  .agent__name { font-weight: 900; font-size: 24px; letter-spacing: .4px; line-height: 1; color: var(--ink); }
  .agent__title { color: var(--accent); font-size: 13px; font-weight: 700; margin-top: 5px; }
  .agent__rule { width: 270px; height: 2px; background: var(--accent); margin-top: 6px; }
  .brand { display: flex; align-items: center; gap: 12px; margin-top: 11px; }
  .brand__mark { font-weight: 900; font-size: 17px; color: var(--ink); white-space: nowrap; }
  .brand__office { font-size: 12px; line-height: 1.2; }
  .agent__areas { font-size: 14px; margin-top: 9px; }
  .agent__legal { font-size: 8px; line-height: 1.25; width: 265px; margin-top: 4px; }
  .contact { list-style: none; margin-top: 8px; font-size: 12.5px; }
  .contact li { display: flex; align-items: center; gap: 8px; line-height: 1.4; }
  .contact svg { width: 12px; height: 12px; fill: var(--accent); flex: none; }
  .web {
    position: absolute; right: 22px; bottom: 32px;
    color: var(--paper); font-size: 13px;
    transform: rotate(-12deg); transform-origin: right bottom;
  }

  /* back */
  .monogram {
    position: absolute; left: 74px; top: 50px;
    width: 92px; height: 92px; border-radius: 50%;
    background: var(--accent);
  }
  .back__name {
    position: absolute; left: 70px; top: 150px;
    color: var(--paper); font-size: 44px; font-weight: 400; letter-spacing: .5px;
  }
  .back__web {
    position: absolute; left: 190px; top: 214px;
    color: var(--paper); font-size: 14px;
  }
</style>
</head>
<body>

<section class="card card--front">
  <div class="portrait" role="img" aria-label="Portrait photo of the agent in a blue blazer and white shirt"></div>
  <svg class="swoosh" viewBox="0 0 540 310" aria-hidden="true">
    <path class="swoosh__band" d="M0 290 C 200 290 380 240 540 202 L540 310 L0 310 Z"/>
    <path class="swoosh__stripe" d="M240 294 C 370 264 460 224 540 178 L540 198 C 450 238 360 274 240 294 Z"/>
  </svg>

  <div class="agent">
    <h1 class="agent__name">MARCUS BEL VANE</h1>
    <p class="agent__title">Sales Representative</p>
    <div class="agent__rule"></div>
    <div class="brand">
      <span class="brand__mark">Harborline 47</span>
      <p class="brand__office">Quiet Summit Realty Inc<br>Brokerage</p>
    </div>
    <p class="agent__areas">Toronto, Markham, Durham</p>
    <p class="agent__legal">Independently Owned and Operated trademarks owned by Harborline 47 Real Estate LLC used under license or authorized sub-license. 2017 Harborline 47 Canada Limited Partnership</p>
    <ul class="contact">
      <li><svg viewBox="0 0 24 24"><path d="M6.6 10.8a15 15 0 0 0 6.6 6.6l2.2-2.2c.3-.3.7-.4 1-.2 1.1.4 2.3.6 3.6.6.6 0 1 .4 1 1V20c0 .6-.4 1-1 1C10.6 21 3 13.4 3 4c0-.6.4-1 1-1h3.5c.6 0 1 .4 1 1 0 1.3.2 2.5.6 3.6.1.3 0 .7-.2 1z"/></svg>647-555-0143 (Direct)</li>
      <li><svg viewBox="0 0 24 24"><path d="M6 3h12v5H6zM4 9h16a2 2 0 0 1 2 2v6h-4v4H6v-4H2v-6a2 2 0 0 1 2-2zm4 7v3h8v-3z"/></svg>905-555-0178 (Office)</li>
      <li><svg viewBox="0 0 24 24"><path d="M2 5h20v14H2zm2 2v.5l8 5 8-5V7l-8 5z"/></svg>marcus@mbelvanehomes.example</li>
    </ul>
  </div>
  <p class="web">www.MBelvaneHomes.example</p>
</section>

<section class="card card--back">
  <div class="monogram" aria-hidden="true"></div>
  <h2 class="back__name">Marcus Bel Vane</h2>
  <p class="back__web">www.MBelvaneHomes.example</p>
</section>

</body>
</html>
```